Australian Solar Smart Home Provider needs business card design

We need a simple, clean, business card that shows who we are and gives the brand feeling. Please see the website (www.plovenix.com) and the attached logo as well. Please use this logo on the business card. As a business we do residential solar, batteries, smart home technology, and hot water solutions. We want the feeling to be accessible to ages 40-65 but at the same time be a bit on the technologically savvy side.
Also the primary purpose of the business card is to hand of and drive referrals - so we want everyone to have a referral code on the card and that aspect should stand out.
Things we want on the card with an example employee:
Name: Marcus Pellwood
Position: Director of Sales and Marketing
telephone number office: 02 8765 4312
telephone number mobile: 0428 915 603
address: Suite 402, 18 Brindle Lane, Sydney, NSW 2000
website: www.plovenix.com
Target Market(s)
Homeowners aged 35-60
Industry/Entity Type
Residential
Contact Information for Business Card
Name: Marcus Pellwood
website: www.plovenix.com
referral code: Mpellwood
Look and feel

```html
<!DOCTYPE html>
<html lang="en">
<head>
<meta charset="UTF-8">
<title>Plovenix Business Card – Marcus Pellwood</title>
<link rel="stylesheet" href="https://fonts.googleapis.com/css2?family=Open+Sans:wght@400;700&display=swap">
<style>
  :root {
    --backdrop: #8f9092;
    --card: #ffffff;
    --brand-green: #6ab43e;
    --text-grey: #58595b;
    --logo-grey: #6d6e70;
    --card-shadow: rgba(0, 0, 0, 0.35);
  }

  * { box-sizing: border-box; margin: 0; padding: 0; }

  html, body {
    width: 1200px;
    height: 800px;
    overflow: hidden;
  }

  body {
    background: var(--backdrop);
    display: flex;
    align-items: center;
    justify-content: center;
    font-family: "Open Sans", sans-serif;
  }

  .business-card {
    position: relative;
    width: 880px;
    height: 538px;
    background: var(--card);
    border-radius: 22px;
    box-shadow: 0 18px 40px var(--card-shadow);
  }

  .brand {
    position: absolute;
    top: 48px;
    right: 60px;
    display: flex;
    align-items: center;
    gap: 14px;
  }

  .brand-dot {
    width: 42px;
    height: 42px;
    border-radius: 50%;
    background: var(--brand-green);
  }

  .brand-name {
    font-size: 44px;
    font-weight: 700;
    color: var(--logo-grey);
    letter-spacing: -0.5px;
    line-height: 1;
  }

  .contact-block {
    position: absolute;
    left: 70px;
    top: 196px;
    color: var(--text-grey);
  }

  .person-name {
    font-size: 32px;
    font-weight: 700;
    color: var(--brand-green);
    line-height: 1.2;
  }

  .person-role {
    font-size: 20px;
    line-height: 1.3;
    margin-bottom: 26px;
  }

  .contact-list {
    list-style: none;
    font-size: 20px;
    line-height: 1.45;
  }

  .contact-item {
    display: flex;
    align-items: flex-start;
    gap: 16px;
  }

  .contact-icon {
    flex: 0 0 22px;
    width: 22px;
    height: 22px;
    margin-top: 5px;
    fill: var(--brand-green);
  }

  .contact-item.no-icon { padding-left: 38px; }

  .referral-code {
    font-weight: 700;
    color: var(--brand-green);
    margin-left: 6px;
  }
</style>
</head>
<body>
  <article class="business-card">
    <div class="brand">
      <span class="brand-dot"></span>
      <span class="brand-name">plovenix</span>
    </div>

    <section class="contact-block">
      <h1 class="person-name">Marcus Pellwood</h1>
      <p class="person-role">Director of Sales and Marketing</p>

      <ul class="contact-list">
        <li class="contact-item">
          <svg class="contact-icon" viewBox="0 0 24 24" aria-hidden="true">
            <path d="M12 3 2 12h3v8h5v-5h4v5h5v-8h3z"/>
          </svg>
          <span>Suite 402, 18 Brindle Lane<br>Sydney, NSW 2000</span>
        </li>
        <li class="contact-item">
          <svg class="contact-icon" viewBox="0 0 24 24" aria-hidden="true">
            <path d="M3 8c0-2 3-4 9-4s9 2 9 4v2h-5V8H8v2H3z"/>
            <path d="M6 12h12l2 8H4z"/>
          </svg>
          <span>02 8765 4312</span>
        </li>
        <li class="contact-item">
          <svg class="contact-icon" viewBox="0 0 24 24" aria-hidden="true">
            <circle cx="12" cy="12" r="11"/>
            <path fill="#fff" d="M8 6.5c.5-.5 1.3-.4 1.6.2l1 2c.2.5 0 1-.3 1.3l-.8.7c.6 1.4 1.7 2.6 3 3.2l.8-.8c.4-.3.9-.4 1.3-.2l2 1c.6.3.7 1.1.2 1.6l-1 1c-.9.8-2.2.9-3.3.4-2.7-1.3-4.7-3.4-5.9-6-.5-1.1-.3-2.4.5-3.3z"/>
          </svg>
          <span>0428 915 603</span>
        </li>
        <li class="contact-item">
          <svg class="contact-icon" viewBox="0 0 24 24" aria-hidden="true">
            <circle cx="12" cy="12" r="11"/>
            <path fill="none" stroke="#fff" stroke-width="1.5" d="M1 12h22M12 1c-4 4-4 18 0 22M12 1c4 4 4 18 0 22M3 6.5h18M3 17.5h18"/>
          </svg>
          <span>www.plovenix.com</span>
        </li>
        <li class="contact-item no-icon">
          <span>Referral Code:<strong class="referral-code">Mpellwood</strong></span>
        </li>
      </ul>
    </section>
  </article>
</body>
</html>
```